Hearth Keepers Brochure - marketing an innovative home maintenance subscription program

We would like a brochure for this new service offering.
Hearth Keepers offers a subscription based home maintenance program that is quite unique. Everyone goes to the dentist for regular checkups and cleanings, or takes their car for oil changes, but too few pay that much attention to their largest asset - their home. So we fill that niche. We need a good brochure to promote the quarterly maintenance and our general contracting services.

Target Market(s)

Upper-Middle Class, SF Bay Area, Home Owner. Techies without know-how or time, single women, and elderly families or those with vacation homes.

Industry/Entity Type

Handyman and general contracting (residential construction and maintenance)

Font styles to use
Serif

Colors
0054AA
0677BA
7BADD7
CADEEF
E8F1F8

Requirements
Must have
• Basic contact info for www.HearthKeepers.example, some sort of hook, logo, etc.
Nice to have
• Something awesome!
Should not have
• Want classy, not cheap or flashy. Must have good balance for high-end homeowners in San Francisco Bay Area.

```html
<!DOCTYPE html>
<html lang="en">
<head>
<meta charset="utf-8">
<title>Hearth Keepers – Home Maintenance &amp; Service</title>
<link rel="stylesheet" href="https://fonts.googleapis.com/css2?family=Playfair+Display:wght@600&family=Source+Serif+4:opsz,wght@8..60,400&display=swap">
<style>
  :root {
    --deep: #0054AA;
    --mid: #0677BA;
    --sky: #7BADD7;
    --mist: #CADEEF;
    --haze: #E8F1F8;
    --deep-line: #3a7cc4;
    --ink: #14233a;
    --paper: #ffffff;
  }
  * { box-sizing: border-box; margin: 0; padding: 0; }
  html, body { width: 1200px; height: 927px; overflow: hidden; background: var(--paper); }
  .brochure {
    position: relative; width: 1200px; height: 927px; overflow: hidden;
    background: var(--paper);
    font-family: "Source Serif 4", Georgia, serif;
  }
  .backdrop { position: absolute; inset: 0; width: 1200px; height: 927px; }

  .display { font-family: "Playfair Display", Georgia, serif; font-weight: 600; text-transform: uppercase; }

  .hero-title {
    position: absolute; left: 39px; top: 38px;
    color: var(--haze); font-size: 36px; line-height: 45px; letter-spacing: 0;
  }

  .intro {
    position: absolute; left: 27px; top: 314px; width: 480px;
    font-size: 23px; line-height: 31px; color: var(--ink);
  }

  .service { position: absolute; display: flex; align-items: center; height: 119px; }
  .service-photo { width: 186px; height: 119px; border: 4px solid var(--mid); flex: none; }
  .service-label {
    margin-left: 18px; color: var(--deep); font-size: 19px; line-height: 25px; letter-spacing: 0;
  }

  .photo-kitchen { background: linear-gradient(160deg, #f3efe8 0%, #d9cdbd 55%, #7a5a3e 100%); }
  .photo-drainage { background: linear-gradient(150deg, #8c7c66 0%, #a9a39a 50%, #6e6a66 100%); }
  .photo-deck { background: linear-gradient(140deg, #5d7a2d 0%, #8a8f80 55%, #c9c9c4 100%); }
  .photo-vent { background: linear-gradient(135deg, #e4e6e8 0%, #f4f5f6 50%, #c9ccd0 100%); }
  .photo-door { background: linear-gradient(90deg, #2a1f1a 0%, #5a4030 45%, #e9d8c6 100%); }
  .photo-attic { background: radial-gradient(circle at 50% 60%, #8d7f70 0%, #4b3e33 45%, #231b16 100%); }

  .panel { position: absolute; left: 838px; top: 306px; width: 325px; color: #ffffff; }
  .panel-title { color: var(--mist); font-size: 38px; line-height: 46px; letter-spacing: 0; }
  .panel-copy { margin-top: 8px; font-size: 16.5px; line-height: 21.4px; }
  .panel-copy p { margin-bottom: 21px; }
  .panel-copy p.lead { margin-bottom: 10px; }

  .promise { position: absolute; left: 838px; top: 818px; display: flex; align-items: flex-start; }
  .promise-mark { width: 33px; height: 33px; background: var(--sky); margin-top: 6px; flex: none; }
  .promise-text { margin-left: 14px; color: var(--mist); font-size: 21px; line-height: 26px; letter-spacing: 0; }

  .web {
    position: absolute; right: 22px; top: 884px;
    color: var(--haze); font-size: 15px; line-height: 20px;
  }

  .brand { position: absolute; left: 33px; top: 864px; display: flex; align-items: center; }
  .brand-mark { width: 32px; height: 32px; background: var(--mid); margin-right: 10px; }
  .brand-name { color: var(--deep); font-size: 33px; line-height: 42px; letter-spacing: 0; }
</style>
</head>
<body>
<main class="brochure">

  <svg class="backdrop" viewBox="0 0 1200 927">
    <path fill="var(--deep)" d="M0 0 H1200 V927 H800 V296 C640 302 480 282 330 228 L262 188 L0 188 Z"/>
    <path fill="var(--mid)" d="M250 0 H1200 V42 C1120 180 970 286 790 290 C600 294 420 262 262 188 Z"/>
    <path fill="var(--sky)" d="M250 0 H1200 V30 C1115 172 965 280 785 284 C600 288 420 256 264 182 Z"/>
    <g role="img" aria-label="Photo of a gloved hand tightening a chrome drain pipe under a sink">
      <defs>
        <linearGradient id="heroTone" x1="0" y1="0" x2="1" y2="0.4">
          <stop offset="0" stop-color="#3d3b3a"/>
          <stop offset="0.35" stop-color="#b9b6b2"/>
          <stop offset="0.6" stop-color="#e6e3de"/>
          <stop offset="0.8" stop-color="#a86a3e"/>
          <stop offset="1" stop-color="#2c2a2a"/>
        </linearGradient>
      </defs>
      <path fill="url(#heroTone)" d="M250 0 H1200 V14 C1110 160 960 270 780 274 C600 278 420 246 268 176 Z"/>
    </g>
    <circle cx="127" cy="44" r="208" fill="var(--deep)"/>
    <circle cx="127" cy="44" r="196" fill="none" stroke="var(--deep-line)" stroke-width="2"/>
    <path fill="var(--sky)" d="M290 927 C450 876 620 856 800 866 C880 870 940 890 990 927 Z"/>
    <path fill="var(--deep)" d="M335 927 C490 888 650 872 800 878 V927 Z"/>
    <path fill="var(--paper)" d="M800 876 C880 880 930 898 965 927 H1005 C965 900 900 880 800 872 Z"/>
  </svg>

  <h1 class="hero-title display">Home<br>Maintenance<br>&amp; Service</h1>

  <p class="intro">Hearth Keepers can also help with larger home improvements such as:</p>

  <section class="service" style="left:25px; top:399px;">
    <div class="service-photo photo-kitchen" role="img" aria-label="Photo of a bright remodeled kitchen with island and pendant lights"></div>
    <h2 class="service-label display">Kitchen and<br>Bath Remodels</h2>
  </section>
  <section class="service" style="left:424px; top:399px;">
    <div class="service-photo photo-drainage" role="img" aria-label="Photo of a drainage trench with perforated pipe and gravel"></div>
    <h2 class="service-label display">Site<br>Drainage</h2>
  </section>
  <section class="service" style="left:25px; top:537px;">
    <div class="service-photo photo-deck" role="img" aria-label="Photo of hands using a nail gun on roof shingles"></div>
    <h2 class="service-label display">New Landscape<br>Installations<br>and Decks</h2>
  </section>
  <section class="service" style="left:424px; top:537px;">
    <div class="service-photo photo-vent" role="img" aria-label="Photo of gloved hands fitting a white air vent grille"></div>
    <h2 class="service-label display">Indoor Air<br>Quality<br>Improvements</h2>
  </section>
  <section class="service" style="left:25px; top:675px;">
    <div class="service-photo photo-door" role="img" aria-label="Photo of a drill installing a door lock"></div>
    <h2 class="service-label display">New Roofs,<br>Siding, Doors<br>and Windows</h2>
  </section>
  <section class="service" style="left:424px; top:675px;">
    <div class="service-photo photo-attic" role="img" aria-label="Photo of an attic interior with wooden rafters"></div>
    <h2 class="service-label display">Home Comfort<br>and HVAC<br>Upgrades</h2>
  </section>

  <aside class="panel">
    <h2 class="panel-title display">We Maintain<br>Your Home</h2>
    <div class="panel-copy">
      <p class="lead">so you don’t have to.</p>
      <p>You take your car in for oil changes.</p>
      <p>You go to the dentist for check-ups. But when was the last time you had your home inspected, or managed, to check over 250 items off your to-do list?</p>
      <p>Hearth Keeping is a philosophy and lifestyle change. We keep your largest asset in great condition, and let you take back your weekends.</p>
      <p>Our unique subscription service combines quarterly inspections and handyman repairs.</p>
      <p>Don’t climb that rickety ladder to clean your gutters or start projects you can’t finish.</p>
    </div>
  </aside>

  <div class="promise">
    <span class="promise-mark"></span>
    <p class="promise-text display">Our team is ready to<br>care for your home.</p>
  </div>

  <p class="web">www.HearthKeepers.example</p>

  <footer class="brand">
    <span class="brand-mark"></span>
    <span class="brand-name display">Hearth Keepers</span>
  </footer>

</main>
</body>
</html>
```